Flyer Design Project

We need a flyer (in Spanish) for:
"Feria Cántaro & Telar Brisa Alta 2013"
This event will be held in Los Angeles CA and would like to attract exhibitors.
Must include the information provided in the word file.
Updates

Target Market(s)

Tequila producers and distributors

Industry/Entity Type

Event

Requirements
Must have
• pictures to be used at your discretion

```html
<!DOCTYPE html>
<html lang="es">
<head>
<meta charset="utf-8">
<title>Feria Cántaro &amp; Telar Brisa Alta 2013</title>
<link href="https://fonts.googleapis.com/css2?family=Archivo+Narrow:ital,wght@1,600&family=Cabin:wght@400;600;700&display=swap" rel="stylesheet">
<style>
  :root {
    --slate: #434c53;
    --slate-dark: #394147;
    --orange: #f39a1f;
    --orange-title: #f7a836;
    --sky: #8fd3f4;
    --ink: #2e3336;
    --white: #ffffff;
  }
  html, body { margin: 0; padding: 0; overflow: hidden; background: var(--slate); }
  .flyer {
    position: relative; width: 850px; height: 1200px; overflow: hidden;
    background: var(--slate); font-family: "Cabin", "Gill Sans", sans-serif; color: var(--ink);
  }
  .backdrop { position: absolute; inset: 0; }
  .title {
    position: absolute; top: 30px; left: 0; width: 850px; margin: 0; text-align: center;
    font-family: "Archivo Narrow", "Arial Narrow", sans-serif; font-style: italic; font-weight: 600;
    font-size: 50px; letter-spacing: 0.5px; color: var(--orange-title);
  }
  .tagline {
    position: absolute; top: 117px; left: 146px; width: 310px; margin: 0;
    font-size: 17px; font-weight: 700; line-height: 21px; color: var(--ink);
  }
  .invite { position: absolute; top: 256px; left: 55px; width: 400px; color: var(--white); }
  .invite-lead { margin: 0; font-size: 16px; line-height: 20px; color: var(--orange); }
  .invite-date { margin: 0; font-size: 18px; line-height: 22px; color: var(--orange); }
  .invite-venue { margin: 0 0 9px; font-size: 16px; line-height: 19px; color: var(--orange); }
  .invite-body { margin: 0; font-size: 11.6px; line-height: 16.2px; }
  .story { position: absolute; top: 543px; left: 390px; width: 424px; }
  .story p {
    margin: 0 0 21px; font-size: 15px; line-height: 21.5px; text-align: justify; text-indent: 48px;
  }
  .contact { position: absolute; top: 1030px; left: 385px; width: 446px; text-align: center; }
  .contact-heading { margin: 0 0 4px; font-size: 12.5px; color: #3d4a52; }
  .contact-columns { display: flex; justify-content: center; }
  .contact-card { width: 210px; font-size: 15px; line-height: 20px; }
  .contact-card.us { text-align: right; padding-right: 12px; border-right: 1px solid #5a6a72; }
  .contact-card.mx { text-align: left; padding-left: 12px; }
  .contact-region { color: #3d4a52; font-size: 14.5px; }
  .contact-phone { font-size: 23px; line-height: 30px; font-weight: 600; letter-spacing: 0.5px; }
  .contact-mail { font-size: 14px; }
  .contact-web { margin: 6px 0 0; font-size: 14px; }
</style>
</head>
<body>
<main class="flyer">
  <svg class="backdrop" width="850" height="1200" viewBox="0 0 850 1200" aria-hidden="false">
    <defs>
      <linearGradient id="cityTone" x1="0" y1="0" x2="0" y2="1">
        <stop offset="0" stop-color="#c9d1d8"/><stop offset="1" stop-color="#8c959b"/>
      </linearGradient>
      <linearGradient id="crowdTone" x1="0" y1="0" x2="1" y2="1">
        <stop offset="0" stop-color="#d9c2ae"/><stop offset="0.5" stop-color="#8a5a3e"/><stop offset="1" stop-color="#c79a7c"/>
      </linearGradient>
      <linearGradient id="agaveTone" x1="0" y1="0" x2="0" y2="1">
        <stop offset="0" stop-color="#c8d6e0"/><stop offset="0.4" stop-color="#6f8a6a"/><stop offset="1" stop-color="#4b5a3f"/>
      </linearGradient>
      <linearGradient id="cellarTone" x1="0" y1="0" x2="1" y2="0">
        <stop offset="0" stop-color="#d8d2c8"/><stop offset="0.6" stop-color="#6b4a2e"/><stop offset="1" stop-color="#3e2a1a"/>
      </linearGradient>
      <linearGradient id="potteryTone" x1="0" y1="0" x2="0" y2="1">
        <stop offset="0" stop-color="#6fa3d6"/><stop offset="0.4" stop-color="#c8702f"/><stop offset="1" stop-color="#9b4a1c"/>
      </linearGradient>
    </defs>

    <rect class="header-band" x="0" y="0" width="850" height="112" fill="var(--slate-dark)"/>

    <rect class="photo-city" role="img" aria-label="Fotografía del centro de Los Ángeles con rascacielos" x="0" y="112" width="452" height="400" fill="url(#cityTone)"/>
    <rect class="photo-crowd" role="img" aria-label="Fotografía de un grupo de amigos brindando con caballitos de tequila" x="452" y="112" width="398" height="340" fill="url(#crowdTone)"/>

    <path class="panel-dark" d="M0,196 C170,190 350,240 452,345 L452,520 L0,520 Z" fill="var(--slate)"/>
    <path class="swoosh-top" d="M0,186 C170,180 360,232 452,336 L452,350 C350,246 170,198 0,204 Z" fill="var(--orange)"/>

    <path class="swoosh-white" d="M80,505 C300,530 520,470 650,440 C720,424 790,412 850,400 L850,448 C760,460 640,470 520,486 C380,505 250,520 80,505 Z" fill="var(--white)"/>
    <path class="swoosh-orange" d="M60,512 C250,535 480,500 620,478 C720,462 800,452 850,448 L850,470 C780,480 660,500 520,515 C350,533 200,535 60,512 Z" fill="var(--orange)"/>

    <path class="panel-sky" d="M372,1200 L372,560 C372,530 410,518 480,512 C620,500 760,478 850,470 L850,1200 Z" fill="var(--sky)"/>

    <rect class="photo-agave" role="img" aria-label="Fotografía de un jimador en un campo de agave azul" x="66" y="537" width="236" height="208" fill="url(#agaveTone)"/>
    <path d="M66,537 L100,537 L66,571 Z" fill="var(--orange)"/>
    <rect class="photo-cellar" role="img" aria-label="Fotografía de maestros tequileros catando en una cava de barricas" x="66" y="757" width="236" height="191" fill="url(#cellarTone)"/>
    <path d="M66,757 L100,757 L66,791 Z" fill="var(--orange)"/>
    <rect class="photo-pottery" role="img" aria-label="Fotografía de cántaros artesanales de barro pintados" x="66" y="970" width="236" height="192" fill="url(#potteryTone)"/>
    <path d="M66,970 L100,970 L66,1004 Z" fill="var(--orange)"/>
  </svg>

  <h1 class="title">Feria Cántaro &amp; Telar Brisa Alta 2013</h1>

  <p class="tagline">¡Vinculando marcas emergentes e innovadoras en una época de descubrimiento de sabores mundiales!</p>

  <section class="invite">
    <p class="invite-lead">Acompáñanos los días</p>
    <p class="invite-date">29 y 30 de agosto 2013</p>
    <p class="invite-venue">a “Jardines del Río Brisa”,</p>
    <p class="invite-body">donde se vincularán consumidores, bares, detallistas, restaurantes y distribuidores, en la matriz de creatividad coctelera, talento culinario, sabores de moda y uno de los mercados más importantes e influyentes del mundo. Los fondos que se recauden de este evento, serán destinados a programas sociales promovidos por la Federación de Clubes Alteños del Sur de California.</p>
  </section>

  <section class="story">
    <p>Chile, España, Escocia, Francia, Argentina, Polonia, México – cuando buscamos qué beber, buscamos en el mundo, y ese mundo termina en nuestros vasos. Queremos lo mejor, lo más sabroso, lo interesante y estamos dispuestos a recorrer grandes distancias para obtenerlo.</p>
    <p>La promoción y la creatividad son, quizás, aún más importantes en tiempos de incertidumbre económica, especialmente cuando se es implacable en la búsqueda de nuevos clientes. “Con unas perspectivas más amplias, más globales, ya sea sondeando tradiciones centenarias, o la exploración de las fronteras de las bebidas de moda, buscando nuevos mercados, o reinventando su marca para mantenerse competitivos.”</p>
    <p>En esta edición especializada en Tequila, vamos a discutir las técnicas, procesos creativos, perfiles de sabor, tecnologías, y los ingredientes que son cada vez más esenciales en la caja de herramientas del Coctelero (Mixologist) del siglo 21.</p>
    <p>Tendremos una competencia de las cuatro variedades de tequila: Blanco, Reposado, Añejo y Extra Añejo, con reconocimiento a los ganadores de cada categoría.</p>
  </section>

  <section class="contact">
    <p class="contact-heading">Para oportunidades de exhibición y patrocinio:</p>
    <div class="contact-columns">
      <div class="contact-card us">
        <div class="contact-region">(USA)</div>
        <div class="contact-name">Rodrigo E. Salcedo – Director</div>
        <div class="contact-phone">+ 818-555-0142</div>
        <div class="contact-mail">rsalcedo@brisaalta.com</div>
      </div>
      <div class="contact-card mx">
        <div class="contact-region">(Mexico)</div>
        <div class="contact-name">Ing. Tomás L. Ibarra</div>
        <div class="contact-phone">33-5550-2764</div>
        <div class="contact-mail">tibarra@brisaalta.com</div>
      </div>
    </div>
    <p class="contact-web">www.brisaalta.com</p>
  </section>
</main>
</body>
</html>
```